Harbin Still Works Bottle Label

Harbin Still Works is a distillery and craft cocktail bar that will be located in Calgary, Alberta, Canada. Here, we create awesome hand crafted spirits like vodka, gin, rum, whiskey, brandy, liqueurs etc. We need bottle labels for 3 different initial products. The names of the products are as follows, Pepper Dash Gin (22% alc/vol), Morvane Dry Gin (40% alc/vol), and Talquen Contemporary Gin (40% alc/vol). It would be preferable to have 3 distinct labels. The alcohol by volume declaration must be on the front display of the label, without having to turn the bottle. There is a logo for Harbin Still Works I would like featured in the front around 1''x1" or 2.5cm x 2.5cm in size. Some last minute changes are being made to the logo so it is not uploaded at this moment. Abstract geometry would be a great fit for the contemporary gin and I have attached an example.Simple or complex designs both encouraged. The Pepper Dash Gin will be in the Moonea style bottle and the other two will be in Apotheker style bottles. Thank you so much to anyone interested in participating and we can't wait to hear from you. This is a great opportunity to showcase your creativity and be involved with future products!
Target Market(s)
Young professionals ages 21-30.
Look and feel

```html
<!DOCTYPE html>
<html lang="en">
<head>
<meta charset="utf-8">
<title>Harbin Still Works – Pepper Dash Gin Labels</title>
<link rel="stylesheet" href="https://fonts.googleapis.com/css2?family=Libre+Baskerville:wght@700&family=Barlow+Condensed:wght@700&display=swap">
<style>
  :root {
    --backdrop: #fec896;
    --paper-cream: #ece8d2;
    --paper-navy: #3a3b58;
    --paper-gold: #d9d098;
    --ink-dark: #1e1e2e;
    --ink-light: #ffffff;
    --dot-navy: #14163e;
    --dot-orange: #f39a1e;
    --dot-red: #e6261f;
    --dot-white: #ffffff;
    --dot-blue: #4d66ad;
    --shadow: rgba(60, 40, 20, 0.45);
  }
  * { margin: 0; padding: 0; box-sizing: border-box; }
  html, body { width: 1200px; height: 1200px; overflow: hidden; }
  body { background: var(--backdrop); position: relative; }

  .label-sheet {
    position: absolute;
    left: 288px; top: 96px;
    display: grid;
    grid-template-columns: repeat(3, 204px);
    grid-template-rows: repeat(2, 486px);
    column-gap: 18px;
    row-gap: 22px;
  }

  .label {
    position: relative;
    width: 204px; height: 486px;
    box-shadow: 10px 10px 9px var(--shadow);
    color: var(--ink-dark);
    --rule: var(--ink-dark);
  }
  .label--cream { background: var(--paper-cream); }
  .label--gold  { background: var(--paper-gold); }
  .label--navy  { background: var(--paper-navy); color: var(--ink-light); --rule: var(--ink-light); }

  .brand-name {
    position: absolute; top: 44px; left: 0; width: 100%;
    text-align: center;
    font-family: "Libre Baskerville", serif; font-weight: 700;
    font-size: 13px; letter-spacing: 0.4px; line-height: 1.2;
  }

  .product-name {
    position: absolute; top: 96px; left: 0; width: 100%;
    text-align: center;
    font-family: "Libre Baskerville", serif; font-weight: 700;
    font-size: 15px; letter-spacing: -0.3px; line-height: 1.2;
  }
  .product-rule {
    position: absolute; top: 118px; left: 22px; width: 160px; height: 4px;
    background: var(--rule);
  }

  .origin {
    position: absolute; top: 126px; left: 22px; width: 160px;
    display: flex; justify-content: space-between;
    font-family: "Libre Baskerville", serif; font-weight: 700;
    font-size: 5.5px; letter-spacing: 0.3px;
  }

  .flavour-dot {
    position: absolute; top: 130px; left: 93px;
    width: 18px; height: 18px; border-radius: 50%;
  }
  .flavour-dot--navy   { background: var(--dot-navy); }
  .flavour-dot--orange { background: var(--dot-orange); }
  .flavour-dot--red    { background: var(--dot-red); }
  .flavour-dot--white  { background: var(--dot-white); }
  .flavour-dot--blue   { background: var(--dot-blue); }

  .pattern-panel {
    position: absolute; top: 172px; left: 12px; width: 180px; height: 272px;
    border: 1.5px solid var(--rule);
  }
  .pattern--teal-orange { background: linear-gradient(160deg, #1a8d8a 0%, #f39a1e 45%, #1b1a44 100%); }
  .pattern--red         { background: linear-gradient(160deg, #a0231d 0%, #d8322a 45%, #f4e9e6 100%); }
  .pattern--coral-blue  { background: linear-gradient(160deg, #4d66ad 0%, #ea6a5e 50%, #f7f1c8 100%); }
  .pattern--cyan-purple { background: linear-gradient(160deg, #6a3d94 0%, #2aa6dc 50%, #f7f4c6 100%); }

  .volume-line {
    position: absolute; top: 456px; left: 14px; width: 176px;
    display: flex; align-items: center; gap: 6px;
    font-family: "Barlow Condensed", sans-serif; font-weight: 700; font-size: 13px;
  }
  .volume-line .rule { flex: 1; height: 2px; background: var(--rule); }
</style>
</head>
<body>
<main class="label-sheet">

  <article class="label label--cream">
    <div class="brand-name">HARBIN<br>STILL WORKS</div>
    <h1 class="product-name">PEPPER DASH GIN</h1>
    <div class="product-rule"></div>
    <div class="origin"><span>CALGARY</span><span>CANADA</span></div>
    <div class="flavour-dot flavour-dot--navy"></div>
    <div class="pattern-panel pattern--teal-orange" role="img" aria-label="Geometric cube pattern in teal, orange and navy"></div>
    <div class="volume-line"><span>750ml</span><span class="rule"></span><span>22% alc</span></div>
  </article>

  <article class="label label--navy">
    <div class="brand-name">HARBIN<br>STILL WORKS</div>
    <h1 class="product-name">PEPPER DASH GIN</h1>
    <div class="product-rule"></div>
    <div class="origin"><span>CALGARY</span><span>CANADA</span></div>
    <div class="flavour-dot flavour-dot--orange"></div>
    <div class="pattern-panel pattern--teal-orange" role="img" aria-label="Geometric cube pattern in teal, orange and navy"></div>
    <div class="volume-line"><span>750ml</span><span class="rule"></span><span>22% alc</span></div>
  </article>

  <article class="label label--cream">
    <div class="brand-name">HARBIN<br>STILL WORKS</div>
    <h1 class="product-name">PEPPER DASH GIN</h1>
    <div class="product-rule"></div>
    <div class="origin"><span>CALGARY</span><span>CANADA</span></div>
    <div class="flavour-dot flavour-dot--red"></div>
    <div class="pattern-panel pattern--red" role="img" aria-label="Geometric cube pattern in red, dark red and white"></div>
    <div class="volume-line"><span>750ml</span><span class="rule"></span><span>22% alc</span></div>
  </article>

  <article class="label label--navy">
    <div class="brand-name">HARBIN<br>STILL WORKS</div>
    <h1 class="product-name">PEPPER DASH GIN</h1>
    <div class="product-rule"></div>
    <div class="origin"><span>CALGARY</span><span>CANADA</span></div>
    <div class="flavour-dot flavour-dot--white"></div>
    <div class="pattern-panel pattern--coral-blue" role="img" aria-label="Geometric cube pattern in coral, blue and cream"></div>
    <div class="volume-line"><span>750ml</span><span class="rule"></span><span>22% alc</span></div>
  </article>

  <article class="label label--gold">
    <div class="brand-name">HARBIN<br>STILL WORKS</div>
    <h1 class="product-name">PEPPER DASH GIN</h1>
    <div class="product-rule"></div>
    <div class="origin"><span>CALGARY</span><span>CANADA</span></div>
    <div class="flavour-dot flavour-dot--blue"></div>
    <div class="pattern-panel pattern--coral-blue" role="img" aria-label="Geometric cube pattern in coral, blue and cream"></div>
    <div class="volume-line"><span>750ml</span><span class="rule"></span><span>22% alc</span></div>
  </article>

  <article class="label label--navy">
    <div class="brand-name">HARBIN<br>STILL WORKS</div>
    <h1 class="product-name">PEPPER DASH GIN</h1>
    <div class="product-rule"></div>
    <div class="origin"><span>CALGARY</span><span>CANADA</span></div>
    <div class="flavour-dot flavour-dot--white"></div>
    <div class="pattern-panel pattern--cyan-purple" role="img" aria-label="Geometric cube pattern in cyan, purple and cream"></div>
    <div class="volume-line"><span>750ml</span><span class="rule"></span><span>22% alc</span></div>
  </article>

</main>
</body>
</html>
```